Overview of Elder Abuse Resources Brochure

We need a 2-page brochure that provides a list of resources for elders in tribal communities in the US and those who care for them. We want it to be simple and easy to read, and easy to see the difference between each resource. We would also like eye-catching images or graphics. Please keep the images on the front, and add any photos or graphics that depict Native American elders. We need both of our logos on the first page, in the far-right column. Please refer to the attached image for our brand colors and a font suggestion. Please keep the three columns on each page, but delete the blank pages in the document.

```html
<!DOCTYPE html>
<html lang="en">
<head>
<meta charset="utf-8">
<title>Services for Elders &amp; People Who Care for Them – Brochure</title>
<link href="https://fonts.googleapis.com/css2?family=Barlow+Semi+Condensed:wght@500;600;700&family=Roboto:wght@300;400;500;700&display=swap" rel="stylesheet">
<style>
:root{
  --teal:#21707a;
  --cyan:#2bb3cf;
  --rust:#b4584c;
  --maroon:#4a1b1b;
  --maroon-2:#5a2320;
  --ink:#1c1c1c;
  --paper:#ffffff;
  --bg:#d9d9d9;
  --band:#d9b3ad;
}
*{box-sizing:border-box;margin:0;padding:0}
html,body{width:1200px;height:2336px;overflow:hidden}
body{background:var(--bg);font-family:'Roboto',sans-serif;color:var(--ink);position:relative}
.spread{position:absolute;left:20px;width:1160px;height:816px;display:grid;grid-template-columns:repeat(3,1fr);background:var(--paper);box-shadow:0 4px 14px rgba(0,0,0,.25)}
.spread--outside{top:312px}
.spread--inside{top:1208px}
.panel{position:relative;height:816px;overflow:hidden}
.band{height:18px;background:var(--band)}
.band--foot{position:absolute;left:0;right:0;bottom:0;height:16px}
.head{font-family:'Barlow Semi Condensed',sans-serif;font-weight:700;text-transform:uppercase;line-height:1.1}
/* outside left */
.respect{padding:34px 36px 0 38px}
.respect h2{font-size:34px;color:var(--teal);margin-bottom:16px}
.respect h2 span{color:var(--rust)}
.respect p{font-size:15.5px;line-height:20px;margin-bottom:20px}
.help-box{margin-top:4px;border:1px solid #bbb}
.help-box__title{background:var(--rust);color:#fff;text-align:center;font-family:'Barlow Semi Condensed',sans-serif;font-weight:700;font-size:23px;padding:2px 0}
.help-box__sub{background:var(--teal);color:#e6f3f4;text-align:center;font-size:15px;line-height:19px;padding:6px 20px 8px;font-weight:300}
.help-box__fill{color:#aaa;text-align:center;font-size:15px;line-height:20px;padding:18px 40px;font-weight:300}
.contact-row{text-align:center;font-size:15px;line-height:20px;padding:9px 0;border-bottom:1px solid #ddd}
.contact-row:last-child{border-bottom:none}
.contact-row .num{font-family:'Barlow Semi Condensed',sans-serif;font-weight:700;font-size:21px;color:var(--teal)}
.contact-row .alert{color:var(--rust);font-weight:700}
.contact-row--big{font-size:19px;font-weight:700}
/* mailing panel */
.mailer{background:var(--teal);color:#fff}
.vtext{position:absolute;writing-mode:vertical-rl;transform:rotate(180deg);font-size:15px;line-height:18px}
.vtext b{font-weight:700}
.vtext--logo{right:40px;top:44px;font-size:20px;line-height:24px}
.vtext--logo strong{font-family:'Barlow Semi Condensed',sans-serif;font-size:44px;line-height:40px;font-weight:700}
.vtext--recipient{left:44px;top:420px}
.vtext--company{left:44px;top:645px}
.vtext--web{left:300px;top:495px}
.vtext--tel{left:300px;top:685px}
/* cover */
.cover-logo{height:122px;display:flex;align-items:center;padding-left:34px;gap:12px}
.brand-mark{width:52px;height:52px;border-radius:50%;background:var(--teal);flex:none}
.brand-name{font-family:'Barlow Semi Condensed',sans-serif;font-weight:700;color:var(--rust);font-size:23px;line-height:24px;text-transform:uppercase}
.cover-title{background:var(--maroon);color:#fff;text-align:center;padding:20px 10px 18px}
.cover-title h1{font-family:'Barlow Semi Condensed',sans-serif;font-weight:500;font-size:31px;line-height:36px}
.cover-title p{font-family:'Barlow Semi Condensed',sans-serif;font-size:13px;margin-top:14px;word-spacing:2px}
.photo{display:block;width:100%}
.photo--cover{height:306px;background:linear-gradient(160deg,#b5603a 0%,#c98455 40%,#7a3b2a 65%,#d6a070 100%)}
.cover-foot{display:flex;padding:16px 24px 0 20px;gap:10px}
.prompts{list-style:none;flex:1}
.prompts li{display:flex;align-items:center;gap:12px;font-size:12.5px;line-height:16px;margin-bottom:12px}
.person-icon{width:30px;height:30px;flex:none}
.partner-badge{width:126px;height:136px;background:#1d2a33;border:2px solid #c9a24a;margin-top:4px}
/* inside */
.stories{padding:40px 26px 0 38px}
.stories h2{font-size:29px;color:var(--rust);margin-bottom:26px}
.stories ul{list-style:none}
.stories li{display:flex;gap:14px;font-size:15.5px;line-height:20px;margin-bottom:18px;align-items:center;padding-right:10px}
.tick{width:17px;height:17px;flex:none}
.stories-band{position:absolute;left:0;right:0;top:512px}
.photo--elders{position:absolute;left:0;right:0;top:530px;height:270px;background:linear-gradient(180deg,#2f4a26 0%,#56733c 35%,#c98a8a 60%,#e0d7d2 85%,#b8a79a 100%)}
.resources{background:linear-gradient(160deg,var(--maroon-2),var(--maroon));color:#fff;padding:38px 40px 0 42px}
.resources h2{font-size:28px;margin-bottom:16px;letter-spacing:.2px}
.res{padding:10px 0 11px;border-bottom:1px solid rgba(255,255,255,.22);font-size:13.5px;line-height:17px;overflow-wrap:anywhere}
.res:last-child{border-bottom:none}
.res h3{color:var(--cyan);font-family:'Roboto',sans-serif;font-weight:700;font-size:14.5px;line-height:17px}
.res b{font-weight:500}
.res .note{font-weight:300}
.care{padding:38px 40px 0 44px}
.care h2{font-size:28px;color:var(--rust);line-height:31px}
.care h4{font-family:'Barlow Semi Condensed',sans-serif;font-weight:600;color:var(--teal);font-size:21px;line-height:25px;margin:2px 0 14px}
.care h3.sect{font-family:'Barlow Semi Condensed',sans-serif;font-weight:700;color:var(--rust);font-size:26px;line-height:30px;margin-top:16px}
.care .res{border-bottom:1px solid #ccc;color:var(--ink);padding:12px 0 14px}
.care .res h3{color:var(--teal)}
.care .res.last{border-bottom:none}
</style>
</head>
<body>

<section class="spread spread--outside">
  <div class="panel respect">
    <h2 class="head">Respect for <span>Elders</span></h2>
    <p>Do you have concerns about an Elder, maybe you see that they are not taking care of themselves, or family only comes once a month when the Elder has money?</p>
    <p>Is an Elder telling you that they are not treated with respect or that someone is bothering them?</p>
    <p>These may be signs of Elder abuse, neglect or exploitation.</p>
    <div class="help-box">
      <div class="help-box__title">FOR HELP CONTACT</div>
      <div class="help-box__sub">Your Tribal Social Services or Elders Department:</div>
      <div class="help-box__fill">Insert contact information for your tribal services, law enforcement, etc.</div>
    </div>
    <div class="contact-row" style="margin-top:14px">The Elder Care Finder for information<br>on Adult Protective Services<br><span class="num">1-800-555-0142</span></div>
    <div class="contact-row contact-row--big">If a serious emergency, <span class="alert">call 911.</span></div>
    <div class="contact-row">For mental health support for yourself<br>or an Elder, <span class="alert">call or text 555-0199</span></div>
    <div class="contact-row">Domestic Violence Hotline<br><span class="num">1.800.555.0163</span></div>
    <div class="band band--foot"></div>
  </div>

  <div class="panel mailer">
    <div class="vtext vtext--logo">Replace with<br><strong>LOGO</strong></div>
    <div class="vtext vtext--recipient"><b>Recipient</b><br>Street Address<br>City, ST ZIP Code</div>
    <div class="vtext vtext--company"><b>Company Name</b><br>Street Address<br>City, ST ZIP</div>
    <div class="vtext vtext--web">Website<br>Email</div>
    <div class="vtext vtext--tel">Telephone<br>Fax</div>
    <div class="band band--foot"></div>
  </div>

  <div class="panel cover">
    <div class="cover-logo">
      <span class="brand-mark"></span>
      <span class="brand-name">Circle of Elders<br>Alliance</span>
    </div>
    <div class="band"></div>
    <div class="cover-title">
      <h1>Services for Elders &amp;<br>People Who Care for Them</h1>
      <p>My Mother &nbsp;|&nbsp; My Father &nbsp;|&nbsp; My Sister &nbsp;|&nbsp; My Grandchild &nbsp;|&nbsp; Myself</p>
    </div>
    <div class="band"></div>
    <div class="photo photo--cover" role="img" aria-label="Photo of a Native American elder and her mother sitting at the doorway of a traditional earthen home in the desert sun"></div>
    <div class="cover-foot">
      <ul class="prompts">
        <li><svg class="person-icon" viewBox="0 0 30 30"><circle cx="15" cy="15" r="15" fill="#b4584c"/><circle cx="15" cy="11" r="4" fill="#fff"/><path d="M8 22c1-4 4-6 7-6s6 2 7 6z" fill="#fff"/></svg>Are you caring for an Elder or a Grandchild?</li>
        <li><svg class="person-icon" viewBox="0 0 30 30"><circle cx="15" cy="15" r="15" fill="#b4584c"/><circle cx="15" cy="11" r="4" fill="#fff"/><path d="M8 22c1-4 4-6 7-6s6 2 7 6z" fill="#fff"/></svg>Are you an Elder who needs help staying at home?</li>
        <li><svg class="person-icon" viewBox="0 0 30 30"><circle cx="15" cy="15" r="15" fill="#b4584c"/><circle cx="15" cy="11" r="4" fill="#fff"/><path d="M8 22c1-4 4-6 7-6s6 2 7 6z" fill="#fff"/></svg>These programs and information can be a helpful resource.</li>
      </ul>
      <div class="partner-badge" role="img" aria-label="Partner badge: Elder Justice Circle Project"></div>
    </div>
    <div class="band band--foot"></div>
  </div>
</section>

<section class="spread spread--inside">
  <div class="panel stories">
    <h2 class="head">Do these stories sound familiar to you?</h2>
    <ul>
      <li><svg class="tick" viewBox="0 0 17 17"><circle cx="8.5" cy="8.5" r="8.5" fill="#21707a"/><path d="M5 8.8l2.4 2.3 4.6-4.8" stroke="#fff" stroke-width="1.8" fill="none"/></svg>My mother gets lost driving home from the store.</li>
      <li><svg class="tick" viewBox="0 0 17 17"><circle cx="8.5" cy="8.5" r="8.5" fill="#21707a"/><path d="M5 8.8l2.4 2.3 4.6-4.8" stroke="#fff" stroke-width="1.8" fill="none"/></svg>I need help getting groceries and with chores at home.</li>
      <li><svg class="tick" viewBox="0 0 17 17"><circle cx="8.5" cy="8.5" r="8.5" fill="#21707a"/><path d="M5 8.8l2.4 2.3 4.6-4.8" stroke="#fff" stroke-width="1.8" fill="none"/></svg>My dad wants to sleep all the time; he doesn’t go out with friends anymore. He stopped drumming.</li>
      <li><svg class="tick" viewBox="0 0 17 17"><circle cx="8.5" cy="8.5" r="8.5" fill="#21707a"/><path d="M5 8.8l2.4 2.3 4.6-4.8" stroke="#fff" stroke-width="1.8" fill="none"/></svg>My sister is raising 3 grandchildren on her own.</li>
      <li><svg class="tick" viewBox="0 0 17 17"><circle cx="8.5" cy="8.5" r="8.5" fill="#21707a"/><path d="M5 8.8l2.4 2.3 4.6-4.8" stroke="#fff" stroke-width="1.8" fill="none"/></svg>My son is disrespecting me. He only comes to visit when my retirement money arrives. He always asks for money.</li>
    </ul>
    <div class="band stories-band"></div>
    <div class="photo photo--elders" role="img" aria-label="Group photo of six Native American elders outdoors in front of a green hedge"></div>
    <div class="band band--foot"></div>
  </div>

  <div class="panel resources">
    <h2 class="head">Resources for Elders</h2>
    <div class="res">
      <h3>Elder Care Finder</h3>
      <b>https://eldercarefinder.example.org<br>Call or Text: 1-800-555-0142<br>Email: help@eldercarefinder.example.org</b><br>
      <span class="note">For help finding support. Ask about services to Tribal Elders.</span>
    </div>
    <div class="res">
      <h3>Memory Care Helpline</h3>
      <b>(24 hours 7 days a week)<br>Call 1-800-555-0187</b><br>
      <span class="note">For support for people living with dementia, caregivers, families and the public. Connect with a live person who can provide information, local resources, crisis assistance and emotional support.</span>
    </div>
    <div class="res">
      <h3>Crisis Support Line</h3>
      <span class="note">For mental health support,</span> <b>call or text 555-0199.</b>
    </div>
    <div class="res">
      <h3>State &amp; Tribal Hotlines | Elder Justice Circle Project</h3>
      <span class="note">To find local resources within your tribe or state that specialize in elder abuse, neglect or exploitation, visit:</span><br>
      <b>https://circleofelders.example.org/justice/state-tribal-hotlines/</b>
    </div>
    <div class="res">
      <h3>Heartline Native Helpline</h3>
      <span class="note">A 24/7 safe, confidential and anonymous domestic and sexual violence helpline for Native Americans and Alaska Natives.</span><br>
      <b>Call 1-844-555-0128<br>https://heartlinehelp.example.org/</b>
    </div>
    <div class="band band--foot"></div>
  </div>

  <div class="panel care">
    <h2 class="head">Resources for Caregivers</h2>
    <h4>Caring for an Older Adult</h4>
    <div class="res">
      <h3>Elder Care Finder</h3>
      <b>https://eldercarefinder.example.org<br>Call or Text: 1-800-555-0142<br>Email: help@eldercarefinder.example.org</b><br>
      <span class="note">For help finding support. Ask about services to Tribal Elders.</span>
    </div>
    <div class="res">
      <h3>Memory Friends | Circle of Elders Alliance</h3>
      <span class="note">An interactive educational program to better understand what dementia is and how it affects people.</span><br>
      <b>https://circleofelders.example.org/memory-friends/</b>
    </div>
    <h3 class="sect">Caring for a Grandchild</h3>
    <h4>Grandparents Raising<br>Grandchildren (Kinship Care)</h4>
    <div class="res">
      <h3>KinshipHomes.example</h3>
      <span class="note">An interactive website that seeks to share all relevant publicly available information impacting grandfamilies.</span>
    </div>
    <div class="res last">
      <h3>Grandparent Resources | Elder Justice Circle Project</h3>
      <span class="note">A list of resources for grandparents raising grandchildren.</span><br>
      <b>https://circleofelders.example.org/justice/<br>grandparent-resources/</b>
    </div>
    <div class="band band--foot"></div>
  </div>
</section>

</body>
</html>
```